It's a new electrical company based in Newcastle NSW. I would like a logo between the two words "BRANO (insert logo) VOLT". I would like the logo to represent electrical and celtic style. For example I have seen a light bulb with a celtic pattern in the middle which looked very good. I would like it to be a white card, mainly black writing and quite basic not too much going on. But maybe have the logo partially red or green?

Reason: Waiting for new e mail address so I can put it on the business card

Industry/Entity Type

Electrical

Contact Information for Business Card

BRANO VOLT
Electrical Contractors
Domestic, commercial, fault finding, testing, re wires, switchboard upgrades
License No: 730482K
Fully Insured
Phone: 0487310294

```html
<!DOCTYPE html>
<html lang="en">
<head>
<meta charset="utf-8">
<title>BRANO VOLT – Business Card</title>
<link rel="stylesheet" href="https://fonts.googleapis.com/css2?family=Tinos:wght@400&family=Crimson+Text:wght@400&family=Marcellus&display=swap">
<style>
  :root {
    --backdrop: #e0e0e0;
    --backdrop-edge: #9a9a9a;
    --card: #ffffff;
    --card-edge: #b5b5b5;
    --brand-red: #d9251d;
    --ink: #1a1a1a;
    --band-yellow: #f7ee1e;
    --band-white: #ffffff;
    --gap: #f2f2f2;
  }
  * { margin: 0; padding: 0; box-sizing: border-box; }
  html, body {
    width: 927px; height: 1200px; overflow: hidden;
    background: var(--backdrop);
  }
  .canvas {
    position: relative; width: 927px; height: 1200px;
    background: var(--backdrop);
    border: 1px solid var(--backdrop-edge);
  }
  .card {
    position: absolute; left: 137px; top: 143px;
    width: 652px; height: 913px;
    background: var(--gap);
    border-radius: 90px 0 0 90px;
    overflow: hidden;
  }
  .card-front {
    position: absolute; left: 0; top: 0; width: 652px; height: 444px;
    background: var(--card);
  }
  .card-back {
    position: absolute; left: 0; top: 471px; width: 652px; height: 442px;
    background: var(--card);
    border: 1px solid var(--card-edge);
    border-left: none;
    border-radius: 0 0 0 90px;
  }
  .brand-mark {
    position: absolute; left: 58px; top: 92px; width: 84px; height: 84px;
  }
  .brand-name {
    position: absolute; left: 185px; top: 48px; width: 452px;
    text-align: center;
    font-family: "Tinos", "Times New Roman", serif;
    font-size: 54px; font-weight: 400; line-height: 1;
    color: var(--brand-red);
    white-space: nowrap;
  }
  .brand-rule {
    position: absolute; left: 219px; top: 136px; width: 383px; height: 3px;
    background: var(--brand-red);
  }
  .services {
    position: absolute; left: 214px; top: 164px;
    font-family: "Crimson Text", "Times New Roman", serif;
    font-size: 42px; line-height: 1;
    color: var(--ink);
    white-space: nowrap;
    transform: scaleX(0.56); transform-origin: left top;
  }
  .details-band {
    position: absolute; left: 0; top: 293px; width: 652px; height: 151px;
    background: var(--brand-red);
    font-family: "Marcellus", "Times New Roman", serif;
    white-space: nowrap;
    line-height: 1;
  }
  .licence {
    position: absolute; left: 45px; top: 18px;
    font-size: 34px; color: var(--band-yellow);
    letter-spacing: 1.5px;
  }
  .contact {
    position: absolute; left: 73px; top: 62px;
    font-size: 33px; color: var(--band-white); letter-spacing: 1.5px;
  }
  .back-flip {
    position: absolute; left: 0; top: 0; width: 100%; height: 100%;
  }
  .back-services {
    position: absolute; left: 126px; top: 30px;
    font-family: "Crimson Text", "Times New Roman", serif;
    font-size: 42px; line-height: 1; color: var(--ink);
    white-space: nowrap;
    transform: scaleX(0.56) scaleY(-1); transform-origin: left center;
  }
  .back-rule {
    position: absolute; left: 131px; top: 135px; width: 379px; height: 3px;
    background: var(--brand-red);
  }
  .back-name {
    position: absolute; left: 131px; top: 146px; width: 379px;
    text-align: center;
    font-family: "Tinos", "Times New Roman", serif;
    font-size: 58px; line-height: 1; color: var(--brand-red);
    white-space: nowrap;
    transform: scaleY(-1);
  }
</style>
</head>
<body>
  <div class="canvas">
    <div class="card">
      <section class="card-front">
        <svg class="brand-mark" viewBox="0 0 84 84" aria-hidden="true">
          <circle cx="42" cy="42" r="40" fill="var(--brand-red)"/>
        </svg>
        <h1 class="brand-name">”BRANO VOLT”</h1>
        <div class="brand-rule"></div>
        <p class="services">Electrical Contractors Domestic, comercial</p>
        <div class="details-band">
          <p class="licence">Switchboard Lisensi No: 730482K</p>
          <p class="contact">Full Insured Phone: 0487310294</p>
        </div>
      </section>
      <section class="card-back">
        <div class="back-flip">
          <p class="back-services">Electrical Contractors Domestic, comercial</p>
          <div class="back-rule"></div>
          <p class="back-name">BRANO VOLT</p>
        </div>
      </section>
    </div>
  </div>
</body>
</html>
```